We have developed a fully functional App called Harborwink. However, it requires a nicer GUI. You can see screenshots of our App on www.harborwink-example.com under "Tutorial". For those of you with Android, you can also install it. When you go to Harborwink-example.com, your phone will automatically redirect you to download. From there, you'll get a better idea of what our App looks like and how your design can make it way better. Please note we expect a design idea for most screens (there's about 8 screens) but do just one screen first and if you win, you can do the other 8 after.

Target Market(s)

People looking for dating / flirting

Industry/Entity Type

Android

Requirements
Must have
• sleek looking

```html
<!DOCTYPE html>
<html lang="en">
<head>
<meta charset="utf-8">
<title>Harborwink – Profile Screens</title>
<link href="https://fonts.googleapis.com/css2?family=Roboto:wght@300;400;500&display=swap" rel="stylesheet">
<style>
  :root {
    --canvas: #e9eeea;
    --ink: #222;
    --muted: #9a9a9a;
    --line: #e3e3e3;
    --band: #e6e6e6;
    --teal-a: #4fd3bd;
    --teal-b: #35c2c6;
    --message-bg: #efefef;
    --hero-a: #2e1a26;
    --hero-b: #4a2533;
    --system: #000;
    --white: #fff;
    --title: #3a4a40;
  }
  * { box-sizing: border-box; margin: 0; padding: 0; }
  html, body { width: 1200px; height: 900px; overflow: hidden; }
  body {
    position: relative;
    background: var(--canvas);
    font-family: "Roboto", Arial, sans-serif;
    color: var(--ink);
  }
  .screen-title {
    position: absolute; top: 58px; width: 400px;
    text-align: center; font-size: 30px; font-weight: 400; color: var(--title);
  }
  .screen {
    position: absolute; top: 200px; width: 320px; height: 590px;
    background: var(--white); overflow: hidden;
    display: flex; flex-direction: column;
    box-shadow: 0 6px 24px rgba(0,0,0,.18);
  }
  .status-bar {
    height: 25px; flex: none; background: var(--system); color: var(--white);
    display: flex; justify-content: flex-end; align-items: center; gap: 4px;
    padding-right: 6px; font-size: 14px;
  }
  .status-bar .time { margin-left: 4px; }
  .toolbar {
    height: 42px; flex: none;
    background: linear-gradient(90deg, var(--teal-a), var(--teal-b));
    display: flex; align-items: center; padding: 0 12px; color: var(--white);
  }
  .toolbar .title { font-size: 16px; margin-left: 8px; flex: 1; }
  .toolbar .actions { display: flex; gap: 16px; align-items: center; }
  .message-bar {
    height: 43px; flex: none; background: var(--message-bg);
    display: flex; align-items: center; justify-content: center; gap: 12px;
    color: var(--muted); font-size: 16px;
    border-bottom: 1px solid var(--line);
  }
  .content { flex: 1; overflow: hidden; display: flex; flex-direction: column; }
  .content > * { flex: none; }
  .hero {
    height: 155px; position: relative;
    background: linear-gradient(120deg, var(--hero-a), var(--hero-b));
    color: var(--white); text-align: center;
  }
  .avatar {
    width: 72px; height: 72px; border-radius: 50%;
    border: 3px solid var(--white); background: #b5b5b5;
    margin: 16px auto 8px;
  }
  .hero .handle { font-size: 17px; }
  .hero .meta { font-size: 11px; color: #ddd; margin-top: 2px; }
  .hero .quote { font-size: 13px; line-height: 21px; padding-top: 12px; }
  .hero .more { font-size: 14px; line-height: 14px; letter-spacing: 1px; margin-top: 6px; }
  .hero .country { font-size: 11px; margin-top: 16px; }
  .hero .link { font-size: 11px; font-weight: 500; margin-top: 7px; }
  .pager {
    position: absolute; left: 0; right: 0; bottom: 8px;
    display: flex; justify-content: center; gap: 5px;
  }
  .pager i { width: 5px; height: 5px; border-radius: 50%; background: rgba(255,255,255,.35); }
  .pager i.on { background: var(--white); }
  .section-title {
    height: 27px; display: flex; align-items: center; padding-left: 14px;
    font-size: 13px; border-bottom: 1px solid var(--line);
  }
  .fact {
    height: 34px; display: flex; align-items: center; gap: 10px;
    padding-left: 14px; font-size: 11px;
  }
  .fact .label { color: var(--muted); }
  .band { height: 28px; background: var(--band); }
  .detail {
    height: 34px; display: flex; align-items: center;
    justify-content: space-between; padding: 0 14px; font-size: 11px;
  }
  .detail .label { color: var(--muted); }
  .likes-box {
    margin: 0 14px; height: 82px; border: 1px solid var(--line);
    padding: 6px 8px; font-size: 11px; line-height: 14px;
  }
  .nav-bar {
    height: 60px; flex: none; background: var(--system);
    display: flex; justify-content: space-around; align-items: center; padding: 0 30px;
  }
</style>
</head>
<body>

<div class="screen-title" style="left:2px">Profile - Header 1</div>
<div class="screen-title" style="left:398px">Profile - Header 2</div>
<div class="screen-title" style="left:794px">Profile - Bottom View</div>

<!-- Screen 1 -->
<section class="screen" style="left:42px">
  <div class="status-bar">
    <svg width="16" height="12" viewBox="0 0 16 12"><path d="M8 12 0 3a12 12 0 0 1 16 0z" fill="#fff"/></svg>
    <svg width="10" height="12" viewBox="0 0 10 12"><path d="M10 0v12H0z" fill="#fff"/></svg>
    <svg width="7" height="13" viewBox="0 0 7 13"><rect x="0" y="1" width="7" height="12" fill="#fff"/><rect x="2" y="0" width="3" height="1" fill="#fff"/></svg>
    <span class="time">12:06</span>
  </div>
  <header class="toolbar">
    <svg width="8" height="12" viewBox="0 0 8 12"><path d="M7 1 2 6l5 5" stroke="#fff" stroke-width="2" fill="none"/></svg>
    <span class="title">Profile</span>
    <div class="actions">
      <svg width="18" height="18" viewBox="0 0 18 18"><circle cx="7" cy="7" r="5.5" stroke="#fff" stroke-width="2" fill="none"/><path d="m11 11 6 6" stroke="#fff" stroke-width="2.4"/></svg>
      <svg width="20" height="20" viewBox="0 0 20 20"><circle cx="10" cy="10" r="9" stroke="#fff" stroke-width="1.8" fill="none"/><circle cx="10" cy="8" r="3.2" fill="#fff"/><path d="M4.5 16a6 6 0 0 1 11 0" fill="#fff"/></svg>
    </div>
  </header>
  <div class="message-bar">
    <svg width="26" height="18" viewBox="0 0 26 18"><rect x="1" y="1" width="24" height="16" fill="none" stroke="#9a9a9a" stroke-width="1.6"/><path d="m1 1 12 9 12-9" fill="none" stroke="#9a9a9a" stroke-width="1.6"/></svg>
    <span>Message</span>
  </div>
  <div class="content">
    <div class="hero" role="img" aria-label="Background photo of blurred night lights behind the profile photo">
      <div class="avatar" role="img" aria-label="Member profile photo"></div>
      <div class="handle">VelvetMarisol</div>
      <div class="meta">F - Bi-Curious, 25</div>
      <div class="pager"><i class="on"></i><i></i></div>
    </div>
    <div class="section-title">About</div>
    <div class="fact"><svg width="16" height="16" viewBox="0 0 16 16"><path d="M8 1 1 8h2v7h4v-4h2v4h4V8h2z" fill="#a8a8a8"/></svg><span><span class="label">Lives in</span> Sacramento, USA</span></div>
    <div class="fact"><svg width="16" height="16" viewBox="0 0 16 16"><path d="M8 15 2 9a3.5 3.5 0 0 1 6-5 3.5 3.5 0 0 1 6 5z" fill="#a8a8a8"/></svg><span>Open Relationship</span></div>
    <div class="fact"><svg width="16" height="16" viewBox="0 0 16 16"><circle cx="8" cy="8" r="7.5" fill="#a8a8a8"/><path d="m4.5 8 2.5 2.5 4.5-5" stroke="#fff" stroke-width="1.6" fill="none"/></svg><span><span class="label">Open to</span> FWB, Maybe More</span></div>
    <div class="fact"><svg width="16" height="16" viewBox="0 0 16 16"><rect x="1" y="3" width="14" height="10" rx="1" fill="#a8a8a8"/><rect x="1" y="5.5" width="14" height="2" fill="#fff"/></svg><span><span class="label">Income:</span> $40,000</span></div>
    <div class="band"></div>
    <div class="section-title">Bio</div>
    <div class="detail"><span class="label">Hair</span><span>Undisclosed</span></div>
    <div class="detail"><span class="label">Body</span><span>Undisclosed</span></div>
  </div>
  <nav class="nav-bar">
    <svg width="32" height="18" viewBox="0 0 32 18"><path d="M7 3h16a6 6 0 0 1 0 12H8M7 3l5-3M7 3l5 3" stroke="#8a8a8a" stroke-width="2" fill="none"/></svg>
    <svg width="34" height="16" viewBox="0 0 34 16"><path d="M1 8 17 1l16 7v7H1z" stroke="#8a8a8a" stroke-width="2" fill="none"/></svg>
    <svg width="32" height="18" viewBox="0 0 32 18"><rect x="1" y="6" width="24" height="11" stroke="#8a8a8a" stroke-width="2" fill="none"/><path d="M6 2h25v10" stroke="#8a8a8a" stroke-width="2" fill="none"/></svg>
  </nav>
</section>

<!-- Screen 2 -->
<section class="screen" style="left:438px">
  <div class="status-bar">
    <svg width="16" height="12" viewBox="0 0 16 12"><path d="M8 12 0 3a12 12 0 0 1 16 0z" fill="#fff"/></svg>
    <svg width="10" height="12" viewBox="0 0 10 12"><path d="M10 0v12H0z" fill="#fff"/></svg>
    <svg width="7" height="13" viewBox="0 0 7 13"><rect x="0" y="1" width="7" height="12" fill="#fff"/><rect x="2" y="0" width="3" height="1" fill="#fff"/></svg>
    <span class="time">12:06</span>
  </div>
  <header class="toolbar">
    <svg width="8" height="12" viewBox="0 0 8 12"><path d="M7 1 2 6l5 5" stroke="#fff" stroke-width="2" fill="none"/></svg>
    <span class="title">Profile</span>
    <div class="actions">
      <svg width="18" height="18" viewBox="0 0 18 18"><circle cx="7" cy="7" r="5.5" stroke="#fff" stroke-width="2" fill="none"/><path d="m11 11 6 6" stroke="#fff" stroke-width="2.4"/></svg>
      <svg width="20" height="20" viewBox="0 0 20 20"><circle cx="10" cy="10" r="9" stroke="#fff" stroke-width="1.8" fill="none"/><circle cx="10" cy="8" r="3.2" fill="#fff"/><path d="M4.5 16a6 6 0 0 1 11 0" fill="#fff"/></svg>
    </div>
  </header>
  <div class="message-bar">
    <svg width="26" height="18" viewBox="0 0 26 18"><rect x="1" y="1" width="24" height="16" fill="none" stroke="#9a9a9a" stroke-width="1.6"/><path d="m1 1 12 9 12-9" fill="none" stroke="#9a9a9a" stroke-width="1.6"/></svg>
    <span>Message</span>
  </div>
  <div class="content">
    <div class="hero" role="img" aria-label="Background photo of blurred night lights behind the profile tagline">
      <div class="quote">"Godess and Temptress<br>lives here!"</div>
      <div class="more">•••</div>
      <div class="country">USA</div>
      <div class="link">social-example.com/velvetmarisol</div>
      <div class="pager"><i></i><i class="on"></i></div>
    </div>
    <div class="section-title">About</div>
    <div class="fact"><svg width="16" height="16" viewBox="0 0 16 16"><path d="M8 1 1 8h2v7h4v-4h2v4h4V8h2z" fill="#a8a8a8"/></svg><span><span class="label">Lives in</span> Sacramento, USA</span></div>
    <div class="fact"><svg width="16" height="16" viewBox="0 0 16 16"><path d="M8 15 2 9a3.5 3.5 0 0 1 6-5 3.5 3.5 0 0 1 6 5z" fill="#a8a8a8"/></svg><span>Open Relationship</span></div>
    <div class="fact"><svg width="16" height="16" viewBox="0 0 16 16"><circle cx="8" cy="8" r="7.5" fill="#a8a8a8"/><path d="m4.5 8 2.5 2.5 4.5-5" stroke="#fff" stroke-width="1.6" fill="none"/></svg><span><span class="label">Open to</span> FWB, Maybe More</span></div>
    <div class="fact"><svg width="16" height="16" viewBox="0 0 16 16"><rect x="1" y="3" width="14" height="10" rx="1" fill="#a8a8a8"/><rect x="1" y="5.5" width="14" height="2" fill="#fff"/></svg><span><span class="label">Income:</span> $40,000</span></div>
    <div class="band"></div>
    <div class="section-title">Bio</div>
    <div class="detail"><span class="label">Hair</span><span>Undisclosed</span></div>
    <div class="detail"><span class="label">Body</span><span>Undisclosed</span></div>
  </div>
  <nav class="nav-bar">
    <svg width="32" height="18" viewBox="0 0 32 18"><path d="M7 3h16a6 6 0 0 1 0 12H8M7 3l5-3M7 3l5 3" stroke="#8a8a8a" stroke-width="2" fill="none"/></svg>
    <svg width="34" height="16" viewBox="0 0 34 16"><path d="M1 8 17 1l16 7v7H1z" stroke="#8a8a8a" stroke-width="2" fill="none"/></svg>
    <svg width="32" height="18" viewBox="0 0 32 18"><rect x="1" y="6" width="24" height="11" stroke="#8a8a8a" stroke-width="2" fill="none"/><path d="M6 2h25v10" stroke="#8a8a8a" stroke-width="2" fill="none"/></svg>
  </nav>
</section>

<!-- Screen 3 -->
<section class="screen" style="left:834px">
  <div class="status-bar">
    <svg width="16" height="12" viewBox="0 0 16 12"><path d="M8 12 0 3a12 12 0 0 1 16 0z" fill="#fff"/></svg>
    <svg width="10" height="12" viewBox="0 0 10 12"><path d="M10 0v12H0z" fill="#fff"/></svg>
    <svg width="7" height="13" viewBox="0 0 7 13"><rect x="0" y="1" width="7" height="12" fill="#fff"/><rect x="2" y="0" width="3" height="1" fill="#fff"/></svg>
    <span class="time">12:06</span>
  </div>
  <header class="toolbar">
    <svg width="8" height="12" viewBox="0 0 8 12"><path d="M7 1 2 6l5 5" stroke="#fff" stroke-width="2" fill="none"/></svg>
    <span class="title">Profile</span>
    <div class="actions">
      <svg width="18" height="18" viewBox="0 0 18 18"><circle cx="7" cy="7" r="5.5" stroke="#fff" stroke-width="2" fill="none"/><path d="m11 11 6 6" stroke="#fff" stroke-width="2.4"/></svg>
      <svg width="20" height="20" viewBox="0 0 20 20"><circle cx="10" cy="10" r="9" stroke="#fff" stroke-width="1.8" fill="none"/><circle cx="10" cy="8" r="3.2" fill="#fff"/><path d="M4.5 16a6 6 0 0 1 11 0" fill="#fff"/></svg>
    </div>
  </header>
  <div class="message-bar">
    <svg width="26" height="18" viewBox="0 0 26 18"><rect x="1" y="1" width="24" height="16" fill="none" stroke="#9a9a9a" stroke-width="1.6"/><path d="m1 1 12 9 12-9" fill="none" stroke="#9a9a9a" stroke-width="1.6"/></svg>
    <span>Message</span>
  </div>
  <div class="content">
    <div class="fact" style="margin-top:-2px"><svg width="16" height="16" viewBox="0 0 16 16"><path d="M8 15 2 9a3.5 3.5 0 0 1 6-5 3.5 3.5 0 0 1 6 5z" fill="#a8a8a8"/></svg><span>Open Relationship</span></div>
    <div class="fact"><svg width="16" height="16" viewBox="0 0 16 16"><circle cx="8" cy="8" r="7.5" fill="#a8a8a8"/><path d="m4.5 8 2.5 2.5 4.5-5" stroke="#fff" stroke-width="1.6" fill="none"/></svg><span><span class="label">Open to</span> FWB, Maybe More</span></div>
    <div class="fact"><svg width="16" height="16" viewBox="0 0 16 16"><rect x="1" y="3" width="14" height="10" rx="1" fill="#a8a8a8"/><rect x="1" y="5.5" width="14" height="2" fill="#fff"/></svg><span><span class="label">Income:</span> $40,000</span></div>
    <div class="band"></div>
    <div class="section-title">Bio</div>
    <div class="detail"><span class="label">Hair</span><span>Undisclosed</span></div>
    <div class="detail"><span class="label">Body</span><span>Undisclosed</span></div>
    <div class="detail"><span class="label">Height</span><span>5'4</span></div>
    <div class="detail"><span class="label">Ethnicity</span><span>Undisclosed</span></div>
    <div class="detail"><span class="label">Likes</span></div>
    <div class="likes-box">I love volleyball. I like hanging out at the beach. I love adventure. I want to explore places.</div>
  </div>
  <nav class="nav-bar">
    <svg width="32" height="18" viewBox="0 0 32 18"><path d="M7 3h16a6 6 0 0 1 0 12H8M7 3l5-3M7 3l5 3" stroke="#8a8a8a" stroke-width="2" fill="none"/></svg>
    <svg width="34" height="16" viewBox="0 0 34 16"><path d="M1 8 17 1l16 7v7H1z" stroke="#8a8a8a" stroke-width="2" fill="none"/></svg>
    <svg width="32" height="18" viewBox="0 0 32 18"><rect x="1" y="6" width="24" height="11" stroke="#8a8a8a" stroke-width="2" fill="none"/><path d="M6 2h25v10" stroke="#8a8a8a" stroke-width="2" fill="none"/></svg>
  </nav>
</section>

</body>
</html>
```